Psychologist website

Simple psychologist website
Site map:
home
self-test
common conditions
children
contact
about
info

Current website:
http://www.corvalepsychology.com.au/

Not in love with logo, or colours etc - open brief
Happy for new font/style/logo for company name

Customer wants clean, credible and warm and friendly look & feel
stock photos OK

Brief:

One home page - simple with 2 or 3 small areas to tease and attract the user and one template page to suit all the other pages

Pages structurally similar to
http://www.wendlecourt.com.au/
In that the home page is different and the other pages are based on one template

Requirements
Must have
• 2 pages - one home page and one template page
• navigation for site map

```html
<!DOCTYPE html>
<html lang="en">
<head>
<meta charset="utf-8">
<title>Corvale &amp; Associates – Clinical Psychologists</title>
<link href="https://fonts.googleapis.com/css2?family=Habibi&family=Questrial&display=swap" rel="stylesheet">
<style>
:root{
  --teal:#6fd4dc;
  --teal-dark:#3fb6c0;
  --ink:#2b2b2b;
  --muted:#555;
  --cream:#fdf5e2;
  --line:#d9d9d9;
  --card-line:#e2e2e2;
  --white:#fff;
  --red:#d8101c;
}
*{box-sizing:border-box;margin:0;padding:0}
html,body{width:896px;height:1200px;overflow:hidden;background:var(--white)}
body{position:relative;font-family:"Questrial",sans-serif;color:var(--ink)}
.abs{position:absolute}

.topbar{left:57px;top:0;width:775px;height:31px;border-bottom:1px solid var(--line)}
.contact-item{top:10px;font-size:10px;color:var(--ink);display:flex;align-items:center;gap:8px;white-space:nowrap}
.contact-item svg{width:11px;height:11px;fill:#555}
.contact-item.email{color:var(--teal-dark)}
.social{top:9px;display:flex;gap:6px}
.social span{width:10px;height:10px;border-radius:50%;background:var(--teal)}
.social span.grey{background:#777}

.brand{left:57px;top:56px}
.brand-name{font-family:"Habibi",serif;font-size:31px;color:var(--ink);line-height:1;white-space:nowrap}
.brand-tag{font-size:13px;letter-spacing:.3px;color:var(--ink);margin-top:3px;white-space:nowrap}

.search{left:653px;top:51px;width:179px;height:29px;border:1px solid var(--line);display:flex}
.search .field{flex:1;display:flex;align-items:center;padding-left:10px}
.search .field svg{width:11px;height:11px}
.search .btn{width:57px;background:var(--teal);color:var(--white);font-family:"Habibi",serif;font-size:11px;display:flex;align-items:center;justify-content:center;letter-spacing:.4px}
.locations{top:98px;right:64px;display:flex;gap:36px;font-size:13px;color:var(--ink);white-space:nowrap}

.nav-rule{left:0;top:167px;width:896px;border-top:1px solid var(--line)}
.nav{left:57px;top:129px;height:39px;display:flex;border:1px solid var(--line);border-bottom:none}
.nav a{font-family:"Habibi",serif;font-size:10.5px;color:var(--ink);text-decoration:none;display:flex;align-items:center;justify-content:center;background:var(--cream);border-right:1px solid var(--line);white-space:nowrap}
.nav a:last-child{border-right:none;justify-content:flex-start;padding-left:13px}
.nav a.plain{background:var(--white)}
.dropdown{left:195px;top:167px;width:106px;height:116px;background:var(--white);border:1px solid var(--line);border-top:none;box-shadow:0 2px 4px rgba(0,0,0,.12);padding:5px 0 0 11px;font-family:"Habibi",serif;font-size:8.5px;line-height:16.6px;white-space:nowrap;overflow:hidden;z-index:2}
.dropdown .on{color:var(--teal)}

.hero{left:57px;top:200px;width:379px;height:378px;border:1px solid #e6dfc8;background:var(--cream)}
.hero-photo{position:absolute;left:0;top:0;width:100%;height:213px;background:linear-gradient(160deg,#8c7b62,#c9b89a 45%,#6e6256)}
.hero-copy{position:absolute;left:189px;top:242px;font-size:13.5px;line-height:16.5px;color:var(--ink);white-space:nowrap}
.hero-copy b{font-weight:700;-webkit-text-stroke:.5px currentColor}
.hero-copy .red{color:var(--red)}
.dots{position:absolute;left:32px;top:333px;display:flex;gap:3px}
.dots span{width:11px;height:11px;border-radius:50%;background:#ccc;border:2px solid #eee;box-shadow:0 0 0 1px #aaa}
.dots span.active{background:#222;border-color:#fff}

.tile{width:180px;height:180px;overflow:hidden}
.tile .photo{height:140px}
.tile .label{height:40px;background:var(--teal);color:var(--white);font-family:"Habibi",serif;font-size:15px;padding:0 10px;display:flex;align-items:center;line-height:15px;white-space:nowrap}
.tile.tall .photo{height:138px}
.tile.tall .label{height:42px}

.welcome-title{left:57px;top:599px;font-family:"Habibi",serif;font-size:17px;font-weight:400;white-space:nowrap}
.welcome-text{left:57px;top:628px;width:776px;font-family:"Habibi",serif;font-size:9.5px;line-height:13.4px}
.more{font-family:"Questrial",sans-serif;font-size:8px;font-weight:700;letter-spacing:.4px;color:var(--teal-dark);white-space:nowrap}
.section-rule{left:57px;top:691px;width:776px;border-top:1px solid var(--line)}
.staff-title{left:57px;top:702px;font-family:"Habibi",serif;font-size:17px;font-weight:400}

.card{top:732px;width:179px;height:228px;border:1px solid var(--card-line);padding:4px}
.card .photo{height:98px;border:1px solid #ccc}
.card .name{font-size:12px;margin:10px 0 0 6px;letter-spacing:.2px;white-space:nowrap}
.card .name.teal{color:var(--teal-dark)}
.card .quals{display:flex;gap:4px;margin:3px 0 0 6px;font-family:"Habibi",serif;font-size:9px;line-height:12px;white-space:nowrap}
.card .quals svg{width:12px;height:10px;flex:none;margin-top:1px}
.card .bio{margin:7px 0 0 3px;font-size:7.2px;line-height:9.2px;color:var(--muted);height:56px;overflow:hidden}
.card .more{position:absolute;right:8px;bottom:8px;font-size:7px}
.card .more.dark{color:var(--ink)}

.reviews-title{left:57px;top:984px;font-family:"Habibi",serif;font-size:19px;font-weight:400}
.arrows{left:800px;top:1007px;display:flex;gap:8px}
.arrows svg{width:8px;height:11px}
.review{top:1034px;width:190px}
.review .avatar{position:absolute;left:3px;top:0;width:47px;height:47px;border-radius:50%;border:2px solid #eee}
.review .quote{position:absolute;left:60px;top:2px;width:130px;font-size:9.4px;line-height:13.6px;color:var(--muted)}
.review .who{position:absolute;left:60px;top:66px;font-size:9px;white-space:nowrap}
.review .who span{color:var(--teal-dark)}

.footer-rule{left:57px;top:1138px;width:776px;border-top:1px solid var(--line)}
.copyright{left:57px;top:1157px;font-family:"Habibi",serif;font-size:10px;white-space:nowrap}
.footer-social{left:788px;top:1160px;display:flex;gap:6px}
.footer-social span{width:9px;height:9px;border-radius:50%;background:#888}
.footer-band{left:0;top:1190px;width:896px;height:10px;background:var(--teal)}

.appointment{left:0;top:640px;width:32px;height:96px;background:var(--teal-dark);border-radius:0 6px 6px 0;display:flex;align-items:center;justify-content:center}
.appointment span{writing-mode:vertical-rl;color:var(--white);font-size:10px;font-weight:700;letter-spacing:1px;-webkit-text-stroke:.4px var(--white)}
</style>
</head>
<body>

<header>
  <div class="abs topbar"></div>
  <div class="abs contact-item" style="left:405px">
    <svg viewBox="0 0 12 12"><path d="M2.5 1l2 2-1 1.5c.8 1.6 2 2.8 3.5 3.5L8.5 7l2 2-1.5 2C5 10.5 1.5 7 1 2.5z"/></svg>(02) 5550 1420
  </div>
  <div class="abs contact-item" style="left:500px">
    <svg viewBox="0 0 12 12"><rect x="3" y="1" width="6" height="3"/><rect x="1" y="4" width="10" height="5" rx="1"/><rect x="3" y="8" width="6" height="3" fill="#fff" stroke="#555"/></svg>(02) 5550 1421
  </div>
  <div class="abs contact-item email" style="left:601px">
    <svg viewBox="0 0 12 12"><rect x="1" y="2.5" width="10" height="7"/><path d="M1 2.5l5 4 5-4" fill="none" stroke="#fff"/></svg>info@corvalepsychology.com.au
  </div>
  <div class="abs social" style="left:787px" aria-label="Social links">
    <span></span><span class="grey"></span><span></span>
  </div>

  <div class="abs brand">
    <div class="brand-name">Corvale &amp; Associates</div>
    <div class="brand-tag">CLINICAL PSYCHOLOGISTS</div>
  </div>

  <div class="abs search">
    <div class="field"><svg viewBox="0 0 12 12"><circle cx="5" cy="5" r="3.5" fill="none" stroke="#555" stroke-width="1.6"/><path d="M7.5 7.5L11 11" stroke="#555" stroke-width="1.8"/></svg></div>
    <div class="btn">SEARCH</div>
  </div>
  <div class="abs locations"><span>Sydney CBD</span><span>Chatswood</span><span>Westmead</span></div>

  <div class="abs nav-rule"></div>
  <nav class="abs nav">
    <a class="plain" style="width:62px">HOME</a>
    <a style="width:76px">ABOUT US</a>
    <a class="plain" style="width:76px">SERVICES</a>
    <a style="width:78px">SELF-TEST</a>
    <a style="width:144px">COMMON CONDITIONS</a>
    <a style="width:81px">CHILDREN</a>
    <a style="width:46px">FAQ</a>
    <a style="width:75px">CONTACT</a>
    <a style="width:137px">SITEMAP</a>
  </nav>
  <div class="abs dropdown">
    <div>MOOD</div><div>TRAUMA</div><div class="on">ANXIETY</div><div>ADHD</div><div>EATING DISORDERS</div><div>ADDICTIONS</div>
  </div>
</header>

<main>
  <section class="abs hero">
    <div class="hero-photo" role="img" aria-label="Photo of a thoughtful young woman resting her head on her arms"></div>
    <div class="hero-copy">We provide expert<br>treatment for <b>DEPRESSION,</b><br><b class="red">ANXIETY,</b><br><b class="red">EATING DISORDERS,</b><br>and other<br>issues....</div>
    <div class="dots"><span class="active"></span><span></span><span></span><span></span></div>
  </section>

  <a class="abs tile" style="left:454px;top:200px">
    <div class="photo" role="img" aria-label="Photo of doctors in conversation" style="background:linear-gradient(135deg,#e9ecef,#b8c1c8 55%,#5a5e63)"></div>
    <div class="label">Services</div>
  </a>
  <a class="abs tile" style="left:652px;top:200px">
    <div class="photo" role="img" aria-label="Photo of children running on grass" style="background:linear-gradient(180deg,#cfe0a8,#6f9e3c 60%,#4d7e26)"></div>
    <div class="label">Psychstuff For Kids</div>
  </a>
  <a class="abs tile tall" style="left:454px;top:398px">
    <div class="photo" role="img" aria-label="Photo of a therapist taking notes with a worried client" style="background:linear-gradient(135deg,#f2eee6,#d8c7ad 55%,#9a8a76)"></div>
    <div class="label">Congnitive behaviour<br>Therapy</div>
  </a>
  <a class="abs tile tall" style="left:652px;top:398px">
    <div class="photo" role="img" aria-label="Photo of an audience at a lecture" style="background:linear-gradient(180deg,#7a4a22,#b0773a 50%,#3a2414)"></div>
    <div class="label">Latest Lectures</div>
  </a>

  <h1 class="abs welcome-title">Welcome to the World of Clinical Psychologists...!</h1>
  <p class="abs welcome-text">Clinical psychologists, in Sydney, Chatswood, and Westmead, providing cognitive-behaviour therapy (CBT), treatment, and counselling, for depression, anxiety and other issues. Our psychologists provide a comfortable, supportive, and confidential environment for their clients. Our first goal is for you to feel comfortable in exploring issues and sharing sharing your concerns, knowing that you have been heard and understood. It is in this kind of environment that client and therapist can work productively to understand problems and seek solutions... &nbsp;&nbsp;&nbsp;&nbsp;&nbsp;<span class="more">LEARN MORE</span></p>
  <div class="abs section-rule"></div>

  <h2 class="abs staff-title">Our Staffs</h2>
  <span class="abs more" style="left:779px;top:715px">LEARN MORE</span>

  <article class="abs card" style="left:57px">
    <div class="photo" role="img" aria-label="Portrait photo of Dr Miles Corvale" style="background:linear-gradient(135deg,#9a9a9a,#3d3d3d)"></div>
    <div class="name teal">Dr MILES CORVALE</div>
    <div class="quals"><svg viewBox="0 0 12 10"><path d="M6 0l6 3-6 3-6-3z" fill="#444"/><path d="M3 5v3c2 1.5 4 1.5 6 0V5L6 6.5z" fill="#444"/></svg><span>B.A. (Hons)<br>M.Psychol.; PhD</span></div>
    <p class="bio">Miles is the Principal Clinical Psychologist involved in the practice. He has completed degrees in psychology at the Harbourside University (Bachelor of Arts) and the Eastbank University (Master of Arts, Master of Psychology, PhD)....</p>
    <span class="more dark">LEARN MORE</span>
  </article>
  <article class="abs card" style="left:257px">
    <div class="photo" role="img" aria-label="Portrait photo of Leena Marwick" style="background:linear-gradient(135deg,#5e8a3c,#c46a3a 50%,#8a5a32)"></div>
    <div class="name">LEENA MARWICK</div>
    <div class="quals"><svg viewBox="0 0 12 10"><path d="M6 0l6 3-6 3-6-3z" fill="#444"/><path d="M3 5v3c2 1.5 4 1.5 6 0V5L6 6.5z" fill="#444"/></svg><span>B.Sc.(Psych.)(Hons);<br>M.Psychol.</span></div>
    <p class="bio">Leena provides both child and adult psychology services within the practice. She is a Clinical Psychologist and member of the National Psychology Guild who obtained her undergradu-ate and masters degrees ...</p>
    <span class="more">LEARN MORE</span>
  </article>
  <article class="abs card" style="left:455px">
    <div class="photo" role="img" aria-label="Portrait photo of Dr Hollis Tane" style="background:linear-gradient(135deg,#dfe6ea,#9fb3bd 55%,#6a4e3c)"></div>
    <div class="name teal">Dr HOLLIS TANE</div>
    <div class="quals"><svg viewBox="0 0 12 10"><path d="M6 0l6 3-6 3-6-3z" fill="#444"/><path d="M3 5v3c2 1.5 4 1.5 6 0V5L6 6.5z" fill="#444"/></svg><span>B.A.(Hons);<br>M.Psychol.; PhD</span></div>
    <p class="bio">Hollis completed her PhD at the Eastbank University before working clinically in a hospital drug and alcohol service. She has also completed a masters degree in clinical psychology, where her training included work in a specialist ...</p>
    <span class="more">LEARN MORE</span>
  </article>
  <article class="abs card" style="left:654px">
    <div class="photo" role="img" aria-label="Portrait photo of Petra Lindqvist" style="background:linear-gradient(135deg,#f4f6f8,#c9d6e0 55%,#8aa2b4)"></div>
    <div class="name">PETRA LINDQVIST</div>
    <div class="quals"><svg viewBox="0 0 12 10"><path d="M6 0l6 3-6 3-6-3z" fill="#444"/><path d="M3 5v3c2 1.5 4 1.5 6 0V5L6 6.5z" fill="#444"/></svg><span>B.Sc.(Psychol.)(Hons);<br>M.Psychol.</span></div>
    <p class="bio">Petra works from the city rooms in Morrow Street. Petra has completed undergraduate and post-graduate degrees in clinical psychology from the Harbourside University. Among her previously held roles, Petra has ...</p>
    <span class="more">LEARN MORE</span>
  </article>

  <h2 class="abs reviews-title">Clients review about our work</h2>
  <div class="abs arrows">
    <svg viewBox="0 0 8 11"><path d="M6 1L2 5.5 6 10" fill="none" stroke="#222" stroke-width="2"/></svg>
    <svg viewBox="0 0 8 11"><path d="M2 1l4 4.5L2 10" fill="none" stroke="#222" stroke-width="2"/></svg>
  </div>

  <div class="abs review" style="left:57px">
    <div class="avatar" role="img" aria-label="Client portrait" style="background:linear-gradient(135deg,#7a4a2e,#d6a07c)"></div>
    <p class="quote">Lorem ipsum dolor sit amet, consectetur adipisicing elit, sed do eiusmod tempor incididunt ut labore et</p>
    <div class="who">Joan Doe, Northmark</div>
  </div>
  <div class="abs review" style="left:256px">
    <div class="avatar" role="img" aria-label="Client portrait" style="background:linear-gradient(135deg,#5a8fa8,#d9b08a)"></div>
    <p class="quote">Lorem ipsum dolor sit amet, consectetur adipisicing elit, sed do eiusmod tempor incididunt ut labore et</p>
    <div class="who">Jessica Doe, <span>Pixelfold</span></div>
  </div>
  <div class="abs review" style="left:454px">
    <div class="avatar" role="img" aria-label="Client portrait" style="background:linear-gradient(135deg,#8a7a5a,#e0c3a4)"></div>
    <p class="quote">Lorem ipsum dolor sit amet, consectetur adipisicing elit, sed do eiusmod tempor incididunt ut labore et</p>
    <div class="who">Jessica Doe, <span>Pixelfold</span></div>
  </div>
  <div class="abs review" style="left:652px">
    <div class="avatar" role="img" aria-label="Client portrait" style="background:linear-gradient(135deg,#d8c08a,#f3e2cf)"></div>
    <p class="quote">Lorem ipsum dolor sit amet, consectetur adipisicing elit, sed do eiusmod tempor incididunt ut labore et</p>
    <div class="who">Bill Doe, <span>Brightlane</span></div>
  </div>
</main>

<a class="abs appointment"><span>APPOINTMENT</span></a>

<footer>
  <div class="abs footer-rule"></div>
  <p class="abs copyright">© 2013 Corvale&amp;Associates. All Rights Reserved.</p>
  <div class="abs footer-social" aria-label="Social links"><span></span><span></span><span></span></div>
  <div class="abs footer-band"></div>
</footer>

</body>
</html>
```